Accounting firm needing business card / letterhead designed
Marcus L. Tembrook, CPA
marcus@lumenfiledesk.com
www.lumenfiledesk.com
482 E Larkin Ave Perrysburg, OH 43566
419-555-0172
Business

```html
<!DOCTYPE html>
<html lang="en">
<head>
<meta charset="utf-8">
<title>Lumen FileDesk — Business Card</title>
<link rel="stylesheet" href="https://fonts.googleapis.com/css2?family=Open+Sans:wght@400;700&display=swap">
<style>
  :root {
    --navy: #27226a;
    --green: #8cc63f;
    --white: #ffffff;
    --paper: #f4f4f4;
    --backdrop: #e6e6e8;
  }
  * { margin: 0; padding: 0; box-sizing: border-box; }
  html, body { width: 1200px; height: 904px; overflow: hidden; }
  body {
    background: var(--backdrop);
    font-family: "Open Sans", sans-serif;
    display: flex;
    flex-direction: column;
    align-items: center;
    justify-content: center;
    gap: 40px;
  }
  .card {
    width: 700px;
    height: 400px;
    position: relative;
    overflow: hidden;
    box-shadow: 0 6px 18px rgba(0,0,0,0.18);
  }
  .card-front {
    background: var(--navy);
    display: flex;
    align-items: center;
    justify-content: center;
  }
  .brand-name {
    font-weight: 700;
    line-height: 1;
    white-space: nowrap;
  }
  .card-front .brand-name { color: var(--white); font-size: 50px; letter-spacing: 1px; }
  .card-back { display: flex; }
  .back-logo-panel {
    width: 330px;
    flex: none;
    background: linear-gradient(135deg, var(--white), var(--paper));
    display: flex;
    align-items: center;
    justify-content: center;
    padding: 0 36px;
    border-right: 5px solid var(--green);
  }
  .back-logo-panel .brand-name { color: var(--navy); font-size: 30px; }
  .back-info-panel {
    flex: 1;
    background: var(--navy);
    color: var(--white);
    padding: 86px 24px 0 44px;
  }
  .person-name {
    color: var(--green);
    font-weight: 700;
    font-size: 20px;
    white-space: nowrap;
    margin-bottom: 16px;
  }
  .address {
    font-size: 14px;
    line-height: 1.45;
    margin-bottom: 24px;
  }
  .contact-list { list-style: none; }
  .contact-item {
    display: flex;
    align-items: center;
    gap: 12px;
    font-size: 14px;
    line-height: 1.7;
    white-space: nowrap;
  }
  .contact-icon { width: 14px; height: 14px; flex: none; }
</style>
</head>
<body>
  <section class="card card-front" aria-label="Card front">
    <span class="brand-name">Lumen FileDesk</span>
  </section>

  <section class="card card-back" aria-label="Card back">
    <div class="back-logo-panel">
      <span class="brand-name">Lumen FileDesk</span>
    </div>
    <div class="back-info-panel">
      <h1 class="person-name">Marcus L. Tembrook, CPA</h1>
      <p class="address">482 E Larkin Ave Perrysburg<br>OH 43566</p>
      <ul class="contact-list">
        <li class="contact-item">
          <svg class="contact-icon" viewBox="0 0 24 24" aria-hidden="true"><path fill="#8cc63f" d="M6.6 10.8a15 15 0 0 0 6.6 6.6l2.2-2.2a1 1 0 0 1 1-.25 11.4 11.4 0 0 0 3.6.57 1 1 0 0 1 1 1V20a1 1 0 0 1-1 1A17 17 0 0 1 3 4a1 1 0 0 1 1-1h3.5a1 1 0 0 1 1 1c0 1.25.2 2.45.57 3.57a1 1 0 0 1-.25 1z"/></svg>
          <span>419-555-0172</span>
        </li>
        <li class="contact-item">
          <svg class="contact-icon" viewBox="0 0 24 24" aria-hidden="true"><rect x="2" y="5" width="20" height="14" rx="2" fill="#8cc63f"/><path d="M3 6l9 7 9-7" fill="none" stroke="#27226a" stroke-width="2"/></svg>
          <span>marcus@lumenfiledesk.com</span>
        </li>
        <li class="contact-item">
          <svg class="contact-icon" viewBox="0 0 24 24" aria-hidden="true"><g fill="none" stroke="#8cc63f" stroke-width="2"><circle cx="12" cy="12" r="10"/><ellipse cx="12" cy="12" rx="4" ry="10"/><path d="M2 12h20"/></g></svg>
          <span>www.lumenfiledesk.com</span>
        </li>
      </ul>
    </div>
  </section>
</body>
</html>
```